Website design for learning and development business

I need a logo for my new business based in Australasia. I am a kiwi who is a creative change maker working in the Learning & development space. I design experiential learning opportunities for businesses to grow and nurture their tribes. I take a holistic look at an organisation and analyse what is needed to build a positive culture with a growth mindset woven into their DNA. I would like to see designs that are based on the following word snaps - creative, interesting, tribal, journey, adaptability, engaging, fluid, architectural, bespoke, courageous, challenging .I have the logo (attached) and I Need a startup business website designed. I am a Learning and development professional who is looking at going out on my own and establishing my own business. I would like a website designed that people would go to to check out what I do, how I do, what skills I have and how to contact me. Also room for a blog/articles.

Target Market(s)

Small to medium business

Industry/Entity Type

Self employed training and consultancy company

Number of Pages Required

5+ page

Requirements
Must have
• home page, about page, contact us page, blog page, search for us page
Nice to have
• Testimonials,

```html
<!DOCTYPE html>
<html lang="en">
<head>
<meta charset="utf-8">
<title>Kinetic Consulting – Learning and Development</title>
<link rel="stylesheet" href="https://fonts.googleapis.com/css2?family=Poppins:wght@500;600;700;800&family=Roboto:wght@400;500&display=swap">
<style>
:root{
  --red:#c8141c;
  --red-dark:#b10f16;
  --orange:#e55a36;
  --orange-light:#ee6b3f;
  --blue:#2c5fb3;
  --navy:#241c7a;
  --green:#3e9c2a;
  --text:#333;
  --muted:#666;
  --light-bg:#f2f2f2;
  --dark:#151b26;
  --white:#fff;
}
*{margin:0;padding:0;box-sizing:border-box}
html,body{width:1200px;height:3615px;overflow:hidden}
body{position:relative;font-family:'Roboto',sans-serif;color:var(--text);background:var(--white)}
.abs{position:absolute}
.heading{font-family:'Poppins',sans-serif;font-weight:700;text-transform:uppercase}
.underline{position:absolute;height:4px;width:56px;background:var(--orange)}
.btn{position:absolute;display:flex;align-items:center;justify-content:center;border-radius:30px;font-family:'Poppins',sans-serif;font-weight:700;font-size:16px;text-transform:uppercase;color:var(--white);background:linear-gradient(180deg,#e0262b,var(--red-dark))}

/* header */
.site-header{position:absolute;left:0;top:0;width:1200px;height:79px;background:var(--white)}
.brand{position:absolute;left:112px;top:24px;display:flex;align-items:center;gap:10px;font-family:'Poppins',sans-serif;font-weight:800;font-size:20px;color:#1b1b1b;letter-spacing:.5px}
.brand-dot{width:22px;height:22px;border-radius:50%;background:var(--green)}
.nav a{position:absolute;top:33px;font-family:'Poppins',sans-serif;font-weight:600;font-size:12px;color:#222;text-decoration:none}
.phone-btn{left:921px;top:15px;width:167px;height:48px;font-size:18px;text-transform:none}

/* hero */
.hero{position:absolute;left:0;top:79px;width:1200px;height:589px;background:linear-gradient(180deg,#f1f1ef 0%,#e9e9e6 70%,#c5ccd4 100%)}
.hero-photo{position:absolute;left:700px;top:40px;width:500px;height:549px;background:radial-gradient(ellipse at 55% 45%,#8aa6c9 0%,#b9c6d3 45%,rgba(233,233,230,0) 75%)}
.hero-title{position:absolute;left:105px;top:68px;font-family:'Poppins',sans-serif;font-weight:700;font-size:46px;line-height:52px}
.t-orange{color:#e8492a}.t-blue{color:var(--blue)}.t-navy{color:var(--navy)}.t-green{color:var(--green)}
.hero-text{position:absolute;left:107px;top:188px;width:500px;font-size:14.5px;line-height:30px;color:#333}
.search-box{position:absolute;left:107px;top:266px;width:571px;height:56px;background:var(--white);border-radius:4px;box-shadow:0 2px 8px rgba(0,0,0,.08)}
.search-box span{position:absolute;left:14px;top:20px;font-size:13px;color:#777}
.search-btn{position:absolute;left:418px;top:7px;width:146px;height:42px;border-radius:2px;font-size:15px}

/* skills */
.skills-art{position:absolute;left:0;top:700px;width:590px;height:528px;background:radial-gradient(circle at 45% 35%,#e8a040 0%,#c8301e 30%,#3e9c2a 60%,rgba(255,255,255,0) 80%);border-radius:40% 50% 45% 30%}
.skills-title{position:absolute;left:601px;top:748px;font-size:33px;color:var(--red)}
.skills-text{position:absolute;left:601px;top:822px;width:472px;font-size:14.5px;line-height:30px;color:#333;text-align:justify}
.skills-btn{left:601px;top:1144px;width:167px;height:48px}

/* what / how */
.panel{position:absolute;top:1298px;width:600px;height:541px;color:var(--white);text-align:center}
.panel-what{left:0;width:595px;background:linear-gradient(135deg,#c5121a,#d41d22)}
.panel-how{left:595px;width:605px;background:linear-gradient(135deg,#e4562f,#ea6a42)}
.panel h2{position:absolute;left:0;right:0;top:76px;font-size:32px}
.panel .underline{left:50%;margin-left:-28px;top:126px;background:var(--white)}
.panel p{position:absolute;left:50%;margin-left:-240px;top:152px;width:480px;font-size:14.5px;line-height:30px}
.panel .btn{left:50%;margin-left:-84px;top:403px;width:167px;height:48px;background:var(--white);color:var(--red)}
.panel-how .btn{color:var(--orange)}

/* blogs */
.section-title{position:absolute;left:0;width:1200px;text-align:center;font-size:33px;color:var(--red)}
.section-title .alt{color:var(--orange)}
.center-line{left:573px}
.blog-card{position:absolute;top:2000px;width:309px;height:424px;background:var(--white);box-shadow:0 2px 10px rgba(0,0,0,.15);border-radius:4px}
.blog-img{position:absolute;left:5px;top:5px;width:299px;height:204px;background:linear-gradient(160deg,#c9d3dc,#6f7e8c)}
.blog-card h3{position:absolute;left:23px;top:228px;width:270px;font-family:'Poppins',sans-serif;font-weight:700;font-size:17.5px;line-height:23px;color:#222;text-transform:uppercase}
.blog-card p{position:absolute;left:23px;top:285px;width:265px;font-size:13px;line-height:20.5px;color:#555}
.blog-rule{position:absolute;left:23px;top:372px;width:263px;height:1px;background:var(--red)}
.blog-meta{position:absolute;left:23px;top:392px;width:263px;display:flex;justify-content:space-between;font-size:13px;color:#555}
.blog-meta .more{color:var(--orange)}
.arrow{position:absolute;top:2199px;width:48px;height:48px;border-radius:50%;background:#dcdcdc;display:flex;align-items:center;justify-content:center}

/* contact */
.contact{position:absolute;left:0;top:2512px;width:1200px;height:555px;background:var(--light-bg)}
.field{position:absolute;background:var(--white);border:1px solid #999;border-radius:3px;font-size:13px;color:#333;padding:15px 18px}
.submit-btn{left:518px;top:421px;width:165px;height:46px}

/* footer */
.footer{position:absolute;left:0;top:3067px;width:1200px;height:548px;background:linear-gradient(180deg,#1a2030,#11151f);color:var(--white)}
.footer-title{position:absolute;left:0;width:1200px;top:74px;text-align:center;font-size:32px;font-weight:600}
.subscribe{position:absolute;left:286px;top:150px;width:642px;height:53px;background:var(--white);border-radius:30px}
.subscribe span{position:absolute;left:48px;top:17px;font-size:15px;color:#999}
.subscribe-btn{left:484px;top:3px;width:155px;height:47px;font-size:16px}
.footer-brand{position:absolute;left:112px;top:330px;display:flex;align-items:center;gap:10px;font-family:'Poppins',sans-serif;font-weight:800;font-size:26px;color:var(--white)}
.col{position:absolute;top:274px}
.col h4{font-family:'Poppins',sans-serif;font-weight:600;font-size:17px;text-transform:uppercase;margin-bottom:10px}
.col li{list-style:none;font-size:14px;height:30px;display:flex;align-items:center;gap:10px}
.chev{font-size:11px;font-weight:700}
.footer-rule{position:absolute;left:101px;top:464px;width:1050px;height:1px;background:#555}
.social{position:absolute;top:487px;width:32px;height:32px;border-radius:50%;background:var(--red)}
.copyright{position:absolute;left:408px;top:487px;font-size:11px;color:var(--white)}
</style>
</head>
<body>

<header class="site-header">
  <div class="brand"><span class="brand-dot"></span>KINETIC CONSULTING</div>
  <nav class="nav">
    <a style="left:438px">HOME</a>
    <a style="left:531px">ABOUT</a>
    <a style="left:591px">CONTACT</a>
    <a style="left:685px">BLOG</a>
    <a style="left:755px">SEARCH FOR US</a>
  </nav>
  <div class="btn phone-btn">+123 555 0148</div>
</header>

<section class="hero">
  <div class="hero-photo" role="img" aria-label="Photo of a smiling professional working on a laptop in front of a white brick wall"></div>
  <h1 class="hero-title"><span class="t-orange">Learning</span> <span class="t-blue">and</span> <span class="t-navy">Development</span><br><span class="t-green">Professional</span></h1>
  <p class="hero-text">Lorem ipsum dolor sit amet, consectetur adipiscing elit, sed do eiusmod tempor incididunt ut labore et dolore magna aliqua.</p>
  <div class="search-box"><span>Enter The Email</span><div class="btn search-btn">Search</div></div>
</section>

<section class="skills">
  <div class="skills-art" role="img" aria-label="Large colourful brand illustration in red, blue, yellow and green"></div>
  <h2 class="heading skills-title">What skills I have</h2>
  <div class="underline" style="left:601px;top:793px"></div>
  <p class="skills-text">Sed ut perspiciatis unde omnis iste natus error sit voluptatem accusantium doloremque laudantium, totam rem aperiam, eaque ipsa quae ab illo inventore veritatis et quasi architecto beatae vitae dicta sunt explicabo. Nemo enim ipsam voluptatem quia voluptas sit aspernatur aut odit aut fugit, sed quia consequuntur magni dolores eos qui ratione voluptatem sequi nesciunt. Neque porro quisquam est, qui dolorem ipsum quia dolor sit amet, consectetur, adipisci velit, sed quia non numquam eius modi tempora incidunt ut labore et dolore magnam aliquam quaerat voluptatem. Ut enim ad minima veniam, quis nostrum exercitationem.</p>
  <div class="btn skills-btn">Learn More</div>
</section>

<section class="panel panel-what" role="img" aria-label="Red tinted photo of a team meeting">
  <h2 class="heading">What I do</h2>
  <div class="underline"></div>
  <p>Sed ut perspiciatis unde omnis iste natus error sit voluptatem accusantium doloremque laudantium, totam rem aperiam, eaque ipsa quae ab illo inventore veritatis et quasi architecto beatae vitae dicta sunt explicabo. Nemo enim ipsam voluptatem quia voluptas sit aspernatur aut odit aut fugit, sed quia consequuntur magni dolores eos qui ratione voluptatem sequi nesciunt. Neque porro quisquam est, qui dolorem ipsum quia dolor sit amet, consectetur, adipisci velit, sed quia non numquam eius modi tempora incidunt ut labore et dolore magnam .</p>
  <div class="btn">Learn More</div>
</section>
<section class="panel panel-how" role="img" aria-label="Orange tinted photo of a workshop">
  <h2 class="heading">How I do</h2>
  <div class="underline"></div>
  <p>Sed ut perspiciatis unde omnis iste natus error sit voluptatem accusantium doloremque laudantium, totam rem aperiam, eaque ipsa quae ab illo inventore veritatis et quasi architecto beatae vitae dicta sunt explicabo. Nemo enim ipsam voluptatem quia voluptas sit aspernatur aut odit aut fugit, sed quia consequuntur magni dolores eos qui ratione voluptatem sequi nesciunt. Neque porro quisquam est, qui dolorem ipsum quia dolor sit amet, consectetur, adipisci velit, sed quia non numquam eius modi tempora incidunt ut labore et dolore magnam .</p>
  <div class="btn">Learn More</div>
</section>

<section class="blogs">
  <h2 class="heading section-title" style="top:1914px">Our Latest <span class="alt">Blogs</span></h2>
  <div class="underline center-line" style="top:1963px;width:54px"></div>

  <div class="arrow" style="left:32px"><svg width="14" height="14" viewBox="0 0 14 14"><path d="M9 2 4 7l5 5" fill="none" stroke="#333" stroke-width="2"/></svg></div>
  <div class="arrow" style="left:1120px"><svg width="14" height="14" viewBox="0 0 14 14"><path d="M5 2l5 5-5 5" fill="none" stroke="#333" stroke-width="2"/></svg></div>

  <article class="blog-card" style="left:111px">
    <div class="blog-img" role="img" aria-label="Photo of colleagues talking around a laptop"></div>
    <h3>Consectetur adipiscing elit, sed do eiusmod</h3>
    <p>Lorem ipsum dolor sit amet, consectetur adipiscing elit, sed do eiusmod tempor incididunt ut labore et dolore</p>
    <div class="blog-rule"></div>
    <div class="blog-meta"><span>by John doe</span><span class="more">More information</span></div>
  </article>
  <article class="blog-card" style="left:445px">
    <div class="blog-img" role="img" aria-label="Photo of two people working at computers in an office"></div>
    <h3>Consectetur adipiscing elit, sed do eiusmod</h3>
    <p>Lorem ipsum dolor sit amet, consectetur adipiscing elit, sed do eiusmod tempor incididunt ut labore et dolore</p>
    <div class="blog-rule"></div>
    <div class="blog-meta"><span>by John doe</span><span class="more">More information</span></div>
  </article>
  <article class="blog-card" style="left:778px">
    <div class="blog-img" role="img" aria-label="Photo of a team gathered around a computer screen"></div>
    <h3>Consectetur adipiscing elit, sed do eiusmod</h3>
    <p>Lorem ipsum dolor sit amet, consectetur adipiscing elit, sed do eiusmod tempor incididunt ut labore et dolore</p>
    <div class="blog-rule"></div>
    <div class="blog-meta"><span>by John doe</span><span class="more">More information</span></div>
  </article>
</section>

<section class="contact">
  <h2 class="heading section-title" style="top:72px">Get in <span class="alt">Touch</span></h2>
  <div class="underline center-line" style="top:122px"></div>
  <div class="field" style="left:202px;top:162px;width:392px;height:46px">First name</div>
  <div class="field" style="left:606px;top:162px;width:392px;height:46px">Last name</div>
  <div class="field" style="left:202px;top:221px;width:392px;height:46px">Email</div>
  <div class="field" style="left:606px;top:221px;width:392px;height:46px">Phone</div>
  <div class="field" style="left:202px;top:281px;width:796px;height:113px">Message</div>
  <div class="btn submit-btn">Submit</div>
</section>

<footer class="footer">
  <h2 class="heading footer-title">Join our mailing list</h2>
  <div class="subscribe"><span>Enter Email Here</span><div class="btn subscribe-btn">Subscribe</div></div>

  <div class="footer-brand"><span class="brand-dot"></span>KINETIC</div>

  <div class="col" style="left:385px">
    <h4>Quick Links</h4>
    <ul><li><span class="chev">»</span>Home</li><li><span class="chev">»</span>Cold Storage</li><li><span class="chev">»</span>Dry Storage</li><li><span class="chev">»</span>Our Team</li></ul>
  </div>
  <div class="col" style="left:601px">
    <h4>Legal</h4>
    <ul><li><span class="chev">»</span>Privacy Policy</li><li><span class="chev">»</span>Terms &amp; Conditions</li><li><span class="chev">»</span>Contact Us</li><li><span class="chev">»</span>Cookie Policy</li></ul>
  </div>
  <div class="col" style="left:836px">
    <h4>Contact Us</h4>
    <ul>
      <li><svg width="12" height="14" viewBox="0 0 12 14"><path d="M6 0a5 5 0 0 0-5 5c0 4 5 9 5 9s5-5 5-9a5 5 0 0 0-5-5zm0 7a2 2 0 1 1 0-4 2 2 0 0 1 0 4z" fill="#fff"/></svg>48 Harbour Lane, Suite 12</li>
      <li style="padding-left:22px">Wellington 6011</li>
      <li style="margin-top:8px"><svg width="13" height="13" viewBox="0 0 13 13"><path d="M3 0l2 3-1.5 1.5a8 8 0 0 0 5 5L10 8l3 2-1 3C5 13 0 8 0 1z" fill="#fff"/></svg>123 555 0148</li>
      <li style="margin-top:12px"><svg width="14" height="11" viewBox="0 0 14 11"><rect width="14" height="11" rx="1" fill="#fff"/><path d="M0 1l7 5 7-5" fill="none" stroke="#151b26" stroke-width="1.3"/></svg>hello@kineticlearning.example</li>
    </ul>
  </div>

  <div class="footer-rule"></div>
  <span class="social" style="left:108px"></span>
  <span class="social" style="left:155px"></span>
  <span class="social" style="left:202px"></span>
  <span class="social" style="left:248px"></span>
  <p class="copyright">© Copyright 2021 &nbsp;Learning and development &nbsp;&nbsp;| &nbsp;&nbsp;All Rights Reserved</p>
</footer>

</body>
</html>
```